Letterhead Design

I would like 2 different letterheads. One with each logo I have attached. Business info:
Prairie Claims Billing, LLC
3478 N Birch
Alder Falls, NE 68994
(866) 555-0143

```html
<!DOCTYPE html>
<html lang="en">
<head>
<meta charset="utf-8">
<title>Prairie Claims Billing, LLC — Letterhead</title>
<link rel="stylesheet" href="https://fonts.googleapis.com/css2?family=Questrial&display=swap">
<style>
  :root {
    --backdrop: #626262;
    --paper: #ffffff;
    --teal: #1aa3b5;
    --ink: #2b2b2b;
    --icon-grey: #8a8a8a;
    --ornament-grey: #6e6e6e;
    --shadow: rgba(0, 0, 0, 0.35);
  }
  * { box-sizing: border-box; margin: 0; padding: 0; }
  html, body {
    width: 1200px;
    height: 1000px;
    overflow: hidden;
    background: var(--backdrop);
  }
  .canvas {
    position: relative;
    width: 1200px;
    height: 1000px;
  }
  .letterhead {
    position: absolute;
    left: 253px;
    top: 50px;
    width: 694px;
    height: 900px;
    background: var(--paper);
    box-shadow: 2px 3px 6px var(--shadow);
  }
  .brand {
    position: absolute;
    left: 52px;
    top: 40px;
    display: flex;
    align-items: center;
    gap: 10px;
  }
  .brand-mark {
    width: 16px;
    height: 16px;
    background: var(--teal);
  }
  .brand-name {
    font-family: "Questrial", sans-serif;
    font-size: 19px;
    color: var(--teal);
    letter-spacing: 0.3px;
  }
  .contact {
    position: absolute;
    left: 502px;
    top: 36px;
    font-family: "Questrial", sans-serif;
    font-style: normal;
    font-size: 12.5px;
    line-height: 15px;
    color: var(--ink);
  }
  .contact-phone {
    display: flex;
    align-items: center;
    gap: 7px;
    padding-left: 1px;
  }
  .phone-icon {
    width: 10px;
    height: 10px;
  }
  .footer-ornament {
    position: absolute;
    left: 293px;
    top: 843px;
    width: 110px;
    height: 42px;
    border-radius: 20px;
    background: radial-gradient(ellipse at center, var(--ornament-grey) 0%, rgba(110,110,110,0.35) 100%);
  }
  .footer-band {
    position: absolute;
    left: 0;
    right: 0;
    bottom: 0;
    height: 9px;
    background: var(--teal);
  }
</style>
</head>
<body>
  <main class="canvas">
    <article class="letterhead">
      <header>
        <div class="brand">
          <span class="brand-mark"></span>
          <span class="brand-name">Prairie Claims Billing, LLC</span>
        </div>
        <address class="contact">
          <div class="contact-phone">
            <svg class="phone-icon" viewBox="0 0 10 10" aria-hidden="true">
              <rect width="10" height="10" rx="1.5" fill="var(--icon-grey)"/>
              <path d="M3 2.2 L4.3 2.2 L4.6 3.6 L3.9 4.2 C4.3 5 5 5.7 5.8 6.1 L6.4 5.4 L7.8 5.7 L7.8 7 C5 7.2 2.8 5 3 2.2 Z" fill="#fff"/>
            </svg>
            <span>(866) 555-0143</span>
          </div>
          <div>Prairie Claims Billing, LLC,</div>
          <div>3478 N Birch, Alder Falls, NE 68994</div>
        </address>
      </header>
      <div class="footer-ornament" role="img" aria-label="Grey pair of leaf sprigs ornament"></div>
      <div class="footer-band"></div>
    </article>
  </main>
</body>
</html>
```